The Willowbrook Nest - a Nannying Agency for Corporate Companies and Professional Families

The Willowbrook Nest (www.thewillowbrooknest.com.au) is Australia's newest nannying agency aimed at corporate organisations and professional families.

I have attached 3 flyers previously designed that can be adapted if possible, or design 3 different flyers with different imaging that are edgy but professional selling the career opportunity or T.W.N. service. The flyers need to be double sided with image and company info on one side and service info on the other (which ill provide). Then the side with images needs to also be made smaller to be used as an advertisement in newsletters, Chatterbox, magazines etc.

Please provide Flyer 1 designs first, and then I will base my decision on this. The remaining 2 flyers will need to be provided by the winning designer after finishing up the 1st flyer design. Total prize money includes the design/source files for all 3 flyers.

Flyer 1 - Aimed at Families - Heading "Do You Need a Nanny - The Willowbrook Nest can help you find the balance?"
this is to advertise how our service can bring balance to family life and enable women to go back to work easily.
wording to state: The Willowbrook Nest is a nannying agency offering tailored child care services that meet the needs of professional families, while taking away the stress of on-boarding a nanny. If you want consistent family balance, good educational development and happy kids, come and join The Willowbrook Nest.
email address: findmeacarer@thewillowbrooknest.com.au
phone: 1300 864 239

Flyer 2 - Aimed at Nannies - Heading "Do You Want a Career As a Nanny?" this is to advertise a career as a nanny and be employed by The Willowbrook Nest.

The attached shows some wording changes to say
The Willowbrook Nest is Australia's newest nannying agency that recognises and rewards their employees, and provides supportive and structured career options in child care.
We offer full-time, part-time and holiday positions - if you want to have fun and be proud of the company you work for, come and join The Willowbrook Nest.
email address: joinourcarers@thewillowbrooknest.com.au
phone: 1300 864 239

Flyer 3 - Aimed at Companies - Heading "Want To Go Back To Work? The Willowbrook Nest can help you find a nanny"
Wording: The Willowbrook Nest is a nannying agency that enables organisations to support employees family life via employment benefit programs across Australia. Our tailored child care services meet the needs of professional families, while taking away the stress of on-boarding a nanny. If you want to provide family benefits to your employees
email address: hello@thewillowbrooknest.com.au
phone: 1300 864 239

Target Market(s)

Family and Company Flyers - Corporate Companies, Professional families, Mothers that want more time, wealthy business people - generally 30+ males and females
Nanny Flyer - people that love working with children, personal assistance, age brackets are 21 - 30 and 40+ males and females.

Industry/Entity Type

It Company

Font styles to use
Serif

Requirements
Must have
• Nanny Flyer - image of nannies promoting a happy, fun, professional culture - i will provide this image
Company Flyer - image could be a women showing 2 different lifestyles, one chaotic with kids, mess, showing guilt, tired, rushed life to childcare. Other half of life is organised, diary, laptop, Pocketel, corporate dress.
Family flyer - one side crazy disorganised, other side organised and balance family life
White background - navy blue font, align to our colour scheme and professional, shick image.
Should not have
• Should not use too much colour, comic illustrations.

```html
<!DOCTYPE html>
<html lang="en">
<head>
<meta charset="utf-8">
<title>The Willowbrook Nest – Do You Need a Nanny</title>
<link href="https://fonts.googleapis.com/css2?family=Cinzel:wght@600;700&family=Libre+Baskerville:wght@700&family=Lato:wght@400;700&display=swap" rel="stylesheet">
<style>
  :root {
    --navy-deep: #0a0f5c;
    --navy: #12148a;
    --navy-bright: #1c24b8;
    --royal: #2f6be8;
    --silver: #c9ccd3;
    --silver-dark: #8d919b;
    --white: #ffffff;
    --ink: #1d1d24;
    --photo-light: #d9d9db;
    --photo-mid: #a9a9ad;
  }
  * { margin: 0; padding: 0; box-sizing: border-box; }
  html, body { width: 849px; height: 1200px; overflow: hidden; background: var(--white); }
  .flyer {
    position: relative;
    width: 849px;
    height: 1200px;
    overflow: hidden;
    background: linear-gradient(180deg, var(--navy-deep) 0%, var(--navy) 35%, var(--navy-bright) 55%);
    font-family: "Lato", sans-serif;
  }
  .family-photo {
    position: absolute;
    left: 0; top: 520px;
    width: 849px; height: 640px;
    background: radial-gradient(ellipse at 45% 45%, var(--photo-light) 0%, #c4c4c7 45%, var(--photo-mid) 100%);
  }
  .waves { position: absolute; left: 0; top: 0; }
  .brand {
    position: absolute; top: 100px; left: 0; width: 100%;
    text-align: center; color: var(--white);
  }
  .brand-name {
    font-family: "Cinzel", serif; font-weight: 600;
    font-size: 36px; letter-spacing: 1px; color: #e8e9f0;
  }
  .brand-tagline {
    margin-top: 10px;
    font-family: "Libre Baskerville", serif; font-weight: 700;
    font-size: 15px; color: var(--white);
  }
  .brand-tagline .divider {
    display: inline-block; width: 1px; height: 20px; background: var(--silver);
    vertical-align: middle; margin: 0 6px;
  }
  .emblem { position: absolute; left: 0; top: 0; }
  .headline {
    position: absolute; top: 782px; width: 100%; text-align: center;
    font-family: "Cinzel", serif; font-weight: 700;
    font-size: 50px; color: var(--navy); line-height: 1;
  }
  .subhead {
    position: absolute; top: 835px; left: 0; width: 100%;
    display: flex; align-items: center; justify-content: center; gap: 10px;
    font-family: "Cinzel", serif; font-weight: 700;
    font-size: 22px; color: var(--navy-bright);
  }
  .subhead .rule { width: 78px; height: 8px; }
  .intro {
    position: absolute; top: 935px; left: 50%; transform: translateX(-50%);
    width: 740px; text-align: center;
    font-weight: 700; font-size: 17.5px; line-height: 32px; color: var(--ink);
  }
  .contact-band { position: absolute; left: 0; top: 1070px; }
  .contact {
    position: absolute; left: 0; width: 100%;
    display: flex; align-items: center; justify-content: center; gap: 12px;
    color: var(--white); font-size: 22px;
  }
  .contact-email { top: 1100px; }
  .contact-phone { top: 1150px; }
  .contact svg { flex: none; }
</style>
</head>
<body>
<main class="flyer">
  <div class="family-photo" role="img" aria-label="Soft black and white photograph of a parent embracing a young child"></div>

  <svg class="waves" width="849" height="1200" viewBox="0 0 849 1200" aria-hidden="true">
    <path d="M0 560 L0 470 C120 470 200 520 260 600 L280 680 C200 600 110 560 0 560 Z" fill="var(--navy)"/>
    <path d="M0 350 C90 330 170 360 240 400 L240 470 C160 420 80 410 0 440 Z" fill="var(--white)"/>
    <path d="M0 395 C80 375 160 395 240 430 L240 455 C160 415 80 410 0 425 Z" fill="var(--royal)"/>
    <path d="M0 440 C80 410 170 430 240 480 L240 560 C170 490 90 470 0 500 Z" fill="#e4e5ea"/>
    <path d="M0 470 C80 450 160 465 230 520 L240 530 C160 480 80 475 0 495 Z" fill="var(--royal)"/>
    <path d="M669 420 C740 380 800 360 849 355 L849 370 C800 380 740 400 669 440 Z" fill="var(--white)"/>
    <path d="M669 455 C740 420 800 405 849 400 L849 440 C800 440 740 460 669 495 Z" fill="var(--royal)"/>
    <path d="M669 495 C740 460 800 450 849 448 L849 610 C790 620 720 610 669 580 Z" fill="#e4e5ea"/>
    <path d="M669 540 C720 520 760 540 740 565 C720 580 700 570 669 570 Z" fill="var(--royal)"/>
    <path d="M669 580 C720 615 790 625 849 615 L849 700 C780 720 720 700 669 650 Z" fill="var(--navy)"/>
  </svg>

  <header class="brand">
    <div class="brand-name">THE WILLOWBROOK NEST</div>
    <div class="brand-tagline">Professional Nannies<span class="divider"></span>Professional Families</div>
  </header>

  <svg class="emblem" width="849" height="1200" viewBox="0 0 849 1200" aria-hidden="false">
    <defs>
      <linearGradient id="frameSilver" x1="0" y1="0" x2="1" y2="1">
        <stop offset="0" stop-color="#f4f5f8"/>
        <stop offset="0.5" stop-color="var(--silver-dark)"/>
        <stop offset="1" stop-color="#e9eaee"/>
      </linearGradient>
      <radialGradient id="panelGlow" cx="0.5" cy="0.45" r="0.6">
        <stop offset="0" stop-color="#f7f7f9"/>
        <stop offset="1" stop-color="#e6e6ea"/>
      </radialGradient>
    </defs>
    <polygon points="429,207 669,346 669,619 429,756 189,619 189,346" fill="url(#frameSilver)"/>
    <polygon points="429,238 642,361 642,604 429,726 216,604 216,361" fill="var(--white)"/>
    <polygon points="429,250 632,367 632,598 429,714 226,598 226,367" fill="url(#panelGlow)" role="img" aria-label="Illustration of balance scales weighing a family member against a work briefcase"/>
  </svg>

  <h1 class="headline">Do You Need a Nanny</h1>
  <div class="subhead">
    <svg class="rule" viewBox="0 0 78 8" aria-hidden="true"><polygon points="0,4 78,0 78,8" fill="var(--navy)"/></svg>
    <span>The Willowbrook Nest can help you find the balance</span>
    <svg class="rule" viewBox="0 0 78 8" aria-hidden="true"><polygon points="78,4 0,0 0,8" fill="var(--navy)"/></svg>
  </div>

  <p class="intro">The Willowbrook Nest is a nannying agency offering tailored child care services that meet the needs of professional families, while taking away the stress of on-boarding a nanny. If you want consistent family balance, good educational development and happy kids, come and join The Willowbrook Nest.</p>

  <svg class="contact-band" width="849" height="130" viewBox="0 0 849 130" aria-hidden="true">
    <path d="M0 48 Q424 -14 849 48 L849 130 L0 130 Z" fill="var(--white)"/>
    <path d="M0 56 Q424 -4 849 56 L849 130 L0 130 Z" fill="var(--navy)"/>
  </svg>

  <div class="contact contact-email">
    <svg width="28" height="18" viewBox="0 0 28 18" aria-hidden="true"><rect x="1" y="1" width="26" height="16" fill="none" stroke="var(--white)" stroke-width="2"/><path d="M1 1 L14 11 L27 1" fill="none" stroke="var(--white)" stroke-width="2"/></svg>
    <span>findmeacarer@thewillowbrooknest.com.au</span>
  </div>
  <div class="contact contact-phone">
    <svg width="20" height="20" viewBox="0 0 20 20" aria-hidden="true"><rect width="20" height="20" rx="4" fill="var(--white)"/><path d="M6 4 L8 4 L9 7 L7.5 8.5 C8.3 10.3 9.7 11.7 11.5 12.5 L13 11 L16 12 L16 14 C16 15 15 16 14 16 C8.5 16 4 11.5 4 6 C4 5 5 4 6 4 Z" fill="var(--navy)"/></svg>
    <span>1300 864 239</span>
  </div>
</main>
</body>
</html>
```